Packaging designed for both the bar and the box for retail and online sales

The name of the product is Plume Crumb. We manufacture a consumer package good product that's a healthy edible cookie dough bar. The product look, feels and tastes like cookie dough. It's sold in the refrigerator section of retail stores next to cookie dough and tundra loaf. The product is Gluten Free, Diary Free and include B-12, Biotin and Collagen. The ingredients are natural. When design this think about who eat cookie dough and how to engage the buyer in purchasing the product.

We needs design packaging designed for both the bar and the box. I have attached the die lines for both products.

Target Market(s)

Our customer is 16-45. Primarily female but really anyone. Middle to upper income. Interest include healthy life style and yoga. Like to eat something sweet but not feel guilty.

Colors

Designer to choose colors to be used in the design.

Requirements
Must have
• Must be clean, warm, inviting. Brand designs I really like are Tundra Loaf.
Should not have
• Should not have a photo of food

```html
<!DOCTYPE html>
<html lang="en">
<head>
<meta charset="utf-8">
<title>Plume Crumb – Bar Wrapper</title>
<link rel="stylesheet" href="https://fonts.googleapis.com/css2?family=Fredoka:wght@500;600&family=Quicksand:wght@700&family=Nunito:wght@800&display=swap">
<style>
  :root {
    --page: #ffffff;
    --wrapper: #f4f4f3;
    --wrapper-edge: #e4e4e2;
    --mint: #6cbf8a;
    --leaf: #8fd1a4;
    --band-green: #3fa766;
    --band-light: #8fd1a4;
    --sun: #f2dc3c;
    --badge-text: #3d8f3a;
    --ink: #2b2b27;
  }
  * { margin: 0; padding: 0; box-sizing: border-box; }
  html, body { width: 1200px; height: 1200px; overflow: hidden; background: var(--page); }
  .canvas { position: relative; width: 1200px; height: 1200px; }

  .wrapper-shape { position: absolute; left: 0; top: 0; }

  .band {
    position: absolute; left: 175px; width: 850px; height: 46px;
    background: linear-gradient(180deg, var(--band-green), var(--band-light) 50%, var(--band-green));
    border-bottom: 4px solid var(--sun);
  }
  .band--top { top: 404px; }
  .band--bottom { top: 690px; border-bottom: none; border-top: 4px solid var(--sun); }

  .foliage {
    position: absolute;
    background: radial-gradient(ellipse at center, rgba(143,209,164,.55), rgba(143,209,164,0) 70%);
  }
  .foliage--left { left: 270px; top: 462px; width: 115px; height: 155px; }
  .foliage--right { left: 815px; top: 462px; width: 115px; height: 155px; }
  .sprig { position: absolute; top: 580px; width: 110px; height: 22px;
    background: linear-gradient(90deg, rgba(143,209,164,0), rgba(143,209,164,.6), rgba(143,209,164,0)); border-radius: 11px; }
  .sprig--left { left: 382px; }
  .sprig--right { left: 708px; }

  .brand-name {
    position: absolute; left: 0; right: 0; top: 462px; text-align: center;
    font-family: "Fredoka", sans-serif; font-weight: 600; font-size: 78px;
    letter-spacing: 1px; color: var(--mint); line-height: 1; text-transform: uppercase;
  }
  .variant {
    position: absolute; left: 0; right: 0; top: 552px; text-align: center;
    font-family: "Quicksand", sans-serif; font-weight: 700; font-size: 44px;
    color: var(--ink); line-height: 1;
  }

  .claims {
    position: absolute; left: 0; right: 0; top: 622px;
    display: flex; justify-content: center; gap: 26px; list-style: none;
  }
  .claim {
    height: 48px; padding: 0 12px;
    border: 3px solid var(--sun); border-radius: 12px;
    display: flex; align-items: center;
    font-family: "Nunito", sans-serif; font-weight: 800; font-size: 17px;
    color: var(--badge-text); background: var(--page); text-transform: uppercase;
  }
</style>
</head>
<body>
<main class="canvas">
  <svg class="wrapper-shape" width="1200" height="1200" viewBox="0 0 1200 1200" aria-hidden="true">
    <path fill="var(--wrapper)" stroke="var(--wrapper-edge)" stroke-width="1"
      d="M175 400 H1025
         L1030 412 L1025 424 L1030 436 L1025 448 L1030 460 L1025 472 L1030 484 L1025 496 L1030 508 L1025 520 L1030 532 L1025 544 L1030 556 L1025 568 L1030 580 L1025 592 L1030 604 L1025 616 L1030 628 L1025 640 L1030 652 L1025 664 L1030 676 L1025 688 L1030 700 L1025 712 L1030 724 L1025 738
         H175
         L170 724 L175 712 L170 700 L175 688 L170 676 L175 664 L170 652 L175 640 L170 628 L175 616 L170 604 L175 592 L170 580 L175 568 L170 556 L175 544 L170 532 L175 520 L170 508 L175 496 L170 484 L175 472 L170 460 L175 448 L170 436 L175 424 L170 412 Z"/>
  </svg>

  <div class="band band--top" role="img" aria-label="Wavy green and yellow stripe pattern"></div>
  <div class="band band--bottom" role="img" aria-label="Wavy green and yellow stripe pattern"></div>

  <div class="foliage foliage--left" role="img" aria-label="Hand-drawn leafy branches"></div>
  <div class="foliage foliage--right" role="img" aria-label="Hand-drawn leafy branches"></div>
  <div class="sprig sprig--left" role="img" aria-label="Small leaf sprig and flower"></div>
  <div class="sprig sprig--right" role="img" aria-label="Small leaf sprig and flower"></div>

  <h1 class="brand-name">Plume Crumb</h1>
  <p class="variant">natural</p>

  <ul class="claims">
    <li class="claim">Gluten Free</li>
    <li class="claim">Diary Free</li>
    <li class="claim">B-12</li>
    <li class="claim">Biotin</li>
    <li class="claim">Collagen</li>
  </ul>
</main>
</body>
</html>
```